Business Card Design

i am looking a business card for a car rental company long with Taxi service also a logo.
Updates

what is the latest with my project

Industry/Entity Type

Business

Contact Information for Business Card

name of the Company is Brenmoor Auto Hire and Cab Services
Address: Harrow Point Village, St. Lorne's Parish Antigua
Tele# 558-2047/6194852-613-9075
Email: tolvipark@quenmail.net

Font styles to use
Script

```html
<!DOCTYPE html>
<html lang="en">
<head>
<meta charset="utf-8">
<title>Brenmoor Auto Hire and Cab Services – Business Card</title>
<link rel="stylesheet" href="https://fonts.googleapis.com/css2?family=Alegreya+Sans:wght@500&family=Arimo:wght@700&family=Source+Sans+3:wght@400&display=swap">
<style>
  :root {
    --card-bg: #f2f2f4;
    --brand-red: #d9312b;
    --band-soft: #eb9a96;
    --brand-green: #1f9a3f;
    --badge-black: #111111;
    --badge-yellow: #f5c400;
    --ink: #2b2b2b;
  }
  html, body {
    margin: 0;
    padding: 0;
    width: 1200px;
    height: 693px;
    overflow: hidden;
    background: var(--card-bg);
  }
  .card {
    position: relative;
    width: 1200px;
    height: 693px;
    background: var(--card-bg);
    overflow: hidden;
  }
  .divider-band {
    position: absolute;
    left: 465px;
    top: 0;
    width: 52px;
    height: 693px;
    background: linear-gradient(90deg, var(--brand-red), var(--band-soft), var(--brand-red));
  }
  .brand-mark {
    position: absolute;
    left: 60px;
    top: 270px;
    width: 414px;
    text-align: center;
  }
  .brand-mark__dot {
    display: block;
    width: 120px;
    height: 120px;
    margin: 0 auto 54px;
    border-radius: 50%;
    background: var(--brand-red);
  }
  .brand-mark__name {
    margin: 0;
    font-family: "Alegreya Sans", sans-serif;
    font-weight: 500;
    font-size: 38px;
    line-height: 1.1;
    color: var(--brand-red);
  }
  .title {
    position: absolute;
    right: 99px;
    top: 76px;
    text-align: right;
  }
  .title__main {
    margin: 0;
    font-family: "Alegreya Sans", sans-serif;
    font-weight: 500;
    font-size: 62px;
    line-height: 1;
    color: var(--brand-red);
  }
  .title__sub {
    margin: 12px 0 0;
    font-family: "Arimo", sans-serif;
    font-weight: 700;
    font-size: 39px;
    line-height: 1;
    color: var(--brand-green);
  }
  .title__badge {
    display: inline-block;
    padding: 2px 8px;
    border-radius: 5px;
    background: var(--badge-black);
    color: var(--badge-yellow);
  }
  .title-rule {
    position: absolute;
    left: 510px;
    right: 0;
    top: 201px;
    height: 4px;
    background: var(--brand-red);
  }
  .contact {
    position: absolute;
    right: 99px;
    top: 490px;
    margin: 0;
    text-align: right;
    font-family: "Source Sans 3", sans-serif;
    font-style: normal;
    font-size: 29px;
    line-height: 40px;
    color: var(--ink);
  }
</style>
</head>
<body>
  <main class="card">
    <div class="divider-band" role="img" aria-label="Vertical decorative divider band in red and white"></div>

    <div class="brand-mark">
      <span class="brand-mark__dot"></span>
      <p class="brand-mark__name">Brenmoor Auto Hire<br>and Cab Services</p>
    </div>

    <header class="title">
      <h1 class="title__main">Brenmoor Auto</h1>
      <p class="title__sub">Hire and <span class="title__badge">CAB</span> Services</p>
    </header>
    <div class="title-rule"></div>

    <address class="contact">
      Address: Harrow Point Village,<br>
      St. Lorne's Parish Antigua.<br>
      Tele# 558-2047 / 6194852-613-9075<br>
      Email: tolvipark@quenmail.net
    </address>
  </main>
</body>
</html>
```